Business Card Design Project

Business Card
We are rebranding with a new logo
Industry/Entity Type
Business
Contact Information for Business Card
Doug Farrow +61 457820913 doug@lumora.com.au P.O. Box 728 Kelmscott QLD 4309
Requirements
Must have
- Logo

```html
<!DOCTYPE html>
<html lang="en">
<head>
<meta charset="utf-8">
<title>Lumora International – Business Card</title>
<link href="https://fonts.googleapis.com/css2?family=Arimo:wght@400;700&display=swap" rel="stylesheet">
<style>
  :root {
    --backdrop: #24272b;
    --card: #ffffff;
    --blue: #0f9bd7;
    --blue-deep: #0a6fa8;
    --orange: #f07d1a;
    --ink: #3a3a3a;
    --muted: #666666;
  }
  * { margin: 0; padding: 0; box-sizing: border-box; }
  html, body {
    width: 1200px;
    height: 902px;
    overflow: hidden;
    background: var(--backdrop);
    font-family: "Arimo", Arial, sans-serif;
  }
  .card {
    position: absolute;
    left: 100px;
    top: 146px;
    width: 1000px;
    height: 610px;
    background: var(--card);
    border-radius: 26px;
    overflow: hidden;
  }
  .card__artwork {
    position: absolute;
    inset: 0;
    width: 100%;
    height: 100%;
  }
  .brand {
    position: absolute;
    right: 70px;
    top: 72px;
    display: flex;
    align-items: center;
    gap: 12px;
    color: var(--blue-deep);
    font-weight: 700;
    font-size: 34px;
    white-space: nowrap;
  }
  .brand__dot {
    width: 18px;
    height: 18px;
    border-radius: 50%;
    background: var(--blue-deep);
  }
  .person {
    position: absolute;
    right: 70px;
    top: 205px;
    text-align: right;
  }
  .person__name {
    color: var(--blue);
    font-weight: 700;
    font-size: 36px;
  }
  .person__role {
    color: var(--muted);
    font-size: 18px;
    margin-top: 4px;
  }
  .tab {
    position: absolute;
    right: -12px;
    top: 198px;
    width: 30px;
    height: 56px;
    border-radius: 10px;
    background: var(--blue);
  }
  .contact {
    position: absolute;
    left: 405px;
    top: 330px;
    list-style: none;
    color: var(--ink);
    font-size: 26px;
    line-height: 1.25;
  }
  .contact__item {
    display: flex;
    align-items: flex-start;
    gap: 16px;
  }
  .contact__item--address { margin-bottom: 34px; }
  .contact__item + .contact__item { margin-top: 6px; }
  .contact__icon {
    width: 22px;
    height: 22px;
    margin-top: 5px;
    fill: var(--blue);
    flex: none;
  }
</style>
</head>
<body>
  <main class="card">
    <svg class="card__artwork" viewBox="0 0 1000 610" role="img" aria-label="Blue and orange swoosh artwork">
      <defs>
        <linearGradient id="artworkTone" x1="0" y1="0" x2="0" y2="1">
          <stop offset="0" stop-color="#1197d4"/>
          <stop offset="0.65" stop-color="#1a8fc9"/>
          <stop offset="1" stop-color="#f39a3a"/>
        </linearGradient>
      </defs>
      <path d="M0 0 H640 C470 70 350 300 340 610 H0 Z" fill="url(#artworkTone)"/>
    </svg>

    <div class="brand">
      <span class="brand__dot"></span>
      <span class="brand__name">Lumora International</span>
    </div>

    <div class="person">
      <div class="person__name">Doug Farrow</div>
      <div class="person__role">Owner</div>
    </div>
    <div class="tab"></div>

    <ul class="contact">
      <li class="contact__item contact__item--address">
        <svg class="contact__icon" viewBox="0 0 24 24"><path d="M12 3 2 12h3v9h5v-6h4v6h5v-9h3z"/></svg>
        <span>P.O. Box 728<br>Kelmscott QLD 4309</span>
      </li>
      <li class="contact__item">
        <svg class="contact__icon" viewBox="0 0 24 24"><path d="M7 1h10a2 2 0 0 1 2 2v18a2 2 0 0 1-2 2H7a2 2 0 0 1-2-2V3a2 2 0 0 1 2-2zm0 3v14h10V4zm5 15.5a1.2 1.2 0 1 0 0 2.4 1.2 1.2 0 0 0 0-2.4z"/></svg>
        <span>+61 457 820 913</span>
      </li>
      <li class="contact__item">
        <svg class="contact__icon" viewBox="0 0 24 24"><path d="M2 5h20v14H2zm2 2v.5l8 5.5 8-5.5V7zm0 3v7h16v-7l-8 5.5z"/></svg>
        <span>doug@lumora.com.au</span>
      </li>
    </ul>
  </main>
</body>
</html>
```